Business Card Design for Training Business

Clear Path Coaching is a new business that delivers training and other services with a focus on topics related to mental health and wellbeing, for example, Mind Care Basics Course, Resilience etc. We have a strong focus on evidence-based psychology and neuroscience. I have a logo which I will upload with the brief, so please consider colours that work well with the logo.
Target Market(s)
Adults, workplaces (particularly government and not-for-profits)
Industry/Entity Type
Business
Contact Information for Business Card
Head Strong TrainingSamantha SellwoodDirector0438 770 bec@clearpathcoaching.com.auwww.headstrongtraining.com.au

```html
<!DOCTYPE html>
<html lang="en">
<head>
<meta charset="utf-8">
<title>Clear Path Coaching — Business Card</title>
<link rel="stylesheet" href="https://fonts.googleapis.com/css2?family=Open+Sans:wdth,wght@75..100,300..600&family=Raleway:wght@200&display=swap">
<style>
  :root {
    --paper: #ffffff;
    --ink-black: #000000;
    --charcoal: #363636;
    --teal: #22bdc1;
    --teal-light: #7dd8da;
    --logo-ring: #3fb8bd;
    --trim-line: #d8d86a;
    --text-light: #ffffff;
  }
  html, body {
    margin: 0;
    padding: 0;
    width: 1200px;
    height: 741px;
    overflow: hidden;
    background: var(--paper);
  }
  .business-card {
    display: block;
    width: 1200px;
    height: 741px;
  }
  .panel-black { fill: var(--ink-black); }
  .panel-charcoal { fill: var(--charcoal); }
  .panel-teal { fill: var(--teal); }
  .panel-teal-light { fill: var(--teal-light); }
  .trim-frame { fill: none; stroke: var(--trim-line); stroke-width: 1.2; }
  .logo-ring { fill: none; stroke: var(--logo-ring); stroke-width: 2; }
  .brand-name {
    font-family: "Raleway", sans-serif;
    font-weight: 200;
    fill: var(--text-light);
  }
  .brand-name__main { font-size: 80px; letter-spacing: 4px; }
  .brand-name__sub { font-size: 28px; letter-spacing: 16px; }
  .contact {
    font-family: "Open Sans", sans-serif;
    font-weight: 400;
    fill: var(--text-light);
    font-stretch: 90%;
  }
  .contact--phone, .contact--email, .contact--address { font-size: 28px; }
  .contact--web { font-size: 22px; }
  .person-name {
    font-family: "Open Sans", sans-serif;
    font-weight: 400;
    font-size: 39px;
    fill: var(--text-light);
    font-stretch: 90%;
  }
  .person-role {
    font-family: "Open Sans", sans-serif;
    font-weight: 300;
    font-size: 23px;
    font-stretch: 75%;
    fill: var(--text-light);
  }
  .icon-badge { fill: var(--text-light); }
  .icon-glyph { fill: var(--teal); }
  .icon-line { fill: none; stroke: var(--teal); stroke-width: 1.6; }
</style>
</head>
<body>
<svg class="business-card" viewBox="0 0 1200 741" xmlns="http://www.w3.org/2000/svg" aria-label="Clear Path Coaching business card for Rebecca Thornbury, Director">
  <rect width="1200" height="741" fill="var(--paper)"/>

  <!-- Background panels -->
  <path class="panel-black" d="M20 20 L853 20 L903 210 Q913 249 874 259 L20 484 Z"/>
  <path class="panel-charcoal" d="M871 20 L1192 20 L1192 176 L969 235 Q930 245 920 206 Z"/>
  <path class="panel-teal" d="M20 502 L878 276 Q917 266 927 305 L1038 727 L20 727 Z"/>
  <path class="panel-teal-light" d="M973 252 L1192 194 L1192 727 L1056 727 L944 301 Q934 262 973 252 Z"/>

  <rect class="trim-frame" x="44" y="44" width="1123" height="657"/>

  <!-- Brand mark -->
  <circle class="logo-ring" cx="185" cy="311" r="104"/>
  <g transform="rotate(-14.7 315 258)">
    <text class="brand-name brand-name__main" x="315" y="258">CLEAR PATH</text>
    <text class="brand-name brand-name__sub" x="322" y="304">COACHING</text>
  </g>

  <!-- Contact details -->
  <text class="contact contact--phone" x="845" y="347" text-anchor="end" transform="rotate(-14.7 845 347)">+353 1 586 2049</text>
  <text class="contact contact--web" x="842" y="412" text-anchor="end" transform="rotate(-14.7 842 412)">www.clearpathcoaching.com.au</text>
  <text class="contact contact--email" x="873" y="442" text-anchor="end" transform="rotate(-14.7 873 442)">bec@clearpathcoaching.com</text>
  <text class="contact contact--address" x="889" y="513" text-anchor="end" transform="rotate(-14.7 889 513)">24 Harbour Lane, Quay Street, Dublin, D04 K318</text>

  <!-- Contact icons -->
  <g class="icon icon--phone">
    <circle class="icon-badge" cx="881" cy="331" r="15"/>
    <path class="icon-glyph" d="M874 323 q2 -2 4 0 l2 3 q1 2 -1 3 l-1 1 q2 4 6 6 l1 -1 q1 -2 3 -1 l3 2 q2 2 0 4 l-2 2 q-4 2 -10 -3 q-6 -6 -6 -11 Z"/>
  </g>
  <g class="icon icon--web">
    <circle class="icon-badge" cx="895" cy="376" r="15"/>
    <circle class="icon-line" cx="895" cy="376" r="9"/>
    <ellipse class="icon-line" cx="895" cy="376" rx="4" ry="9"/>
    <path class="icon-line" d="M886 376 H904 M888 371 H902 M888 381 H902"/>
  </g>
  <g class="icon icon--email">
    <circle class="icon-badge" cx="903" cy="422" r="15"/>
    <rect class="icon-glyph" x="894" y="416" width="18" height="12" rx="1"/>
    <path d="M894 417 L903 424 L912 417" fill="none" stroke="var(--text-light)" stroke-width="1.5"/>
  </g>
  <g class="icon icon--location">
    <circle class="icon-badge" cx="920" cy="467" r="15"/>
    <path class="icon-glyph" d="M920 477 C914 469 913 466 913 463 a7 7 0 0 1 14 0 c0 3 -1 6 -7 14 Z"/>
    <circle cx="920" cy="463" r="2.6" fill="var(--text-light)"/>
  </g>

  <!-- Name and role -->
  <text class="person-name" x="949" y="567" text-anchor="end" transform="rotate(-14.7 949 567)">REBECCA THORNBURY</text>
  <text class="person-role" x="955" y="595" text-anchor="end" transform="rotate(-14.7 955 595)">Director</text>
</svg>
</body>
</html>
```